VELMIT Business Card

VELMIT (www.velmitpools.example) is a veteran in the swimming pool maintenance and repair business..we have served our clients for 15 years and have a research chemist, an electrician, a plumber and a pool building contractor (in part) on staff...We want to provide a business card that has a dual purpose, that people want to keep around, that leaves people speechless in the sense that they understand the mission of and the experience level of the TEAM at VELMIT.

Target Market(s)

persons who enjoy swimming and make it a priority to swim

Industry/Entity Type

Building

Font styles to use
Serif
Sans Serif

Colors
85acd3
3176b5
95b6d8
3276b5
0355a3
0555a3
0255a3
0455a3
85abd2

Requirements
Must have
• name, title, address, email, text
Nice to have
• a die cut shape
Should not have
• cartoons, pictures of pools

```html
<!DOCTYPE html>
<html lang="en">
<head>
<meta charset="utf-8">
<title>VELMIT Business Card</title>
<link rel="stylesheet" href="https://fonts.googleapis.com/css2?family=Open+Sans:wght@400;600;700&display=swap">
<style>
  :root {
    --bg: #ececec;
    --card-white: #ffffff;
    --brand-blue: #338fb5;
    --brand-deep: #1f6f9a;
    --band-light: #45b3e3;
    --text-blue: #3a8fbf;
    --text-muted: #5b9cc4;
    --social: #3276b5;
  }
  * { box-sizing: border-box; margin: 0; padding: 0; }
  html, body { width: 1200px; height: 1000px; overflow: hidden; }
  body {
    background: var(--bg);
    font-family: "Open Sans", Arial, sans-serif;
    position: relative;
  }
  .card {
    position: absolute;
    top: 350px;
    width: 525px;
    height: 300px;
    box-shadow: 0 6px 18px rgba(0,0,0,0.12);
    overflow: hidden;
  }
  .card--front { left: 50px; background: var(--card-white); }
  .card--back { left: 625px; background: var(--brand-blue); color: #fff; }

  .brand { display: flex; align-items: center; gap: 10px; }
  .brand__mark { width: 26px; height: 26px; flex: none; }
  .brand__name { font-weight: 600; letter-spacing: 1px; line-height: 1; }
  .tagline { font-size: 11px; letter-spacing: 1.6px; text-transform: uppercase; white-space: nowrap; }

  .front__brand { position: absolute; left: 40px; top: 34px; }
  .front__brand .brand__mark { background: var(--social); }
  .front__brand .brand__name { font-size: 40px; color: var(--text-blue); }
  .front__tagline { position: absolute; left: 40px; top: 86px; color: var(--text-muted); }

  .person { position: absolute; left: 40px; top: 118px; }
  .person__name { font-size: 17px; font-weight: 700; color: var(--text-blue); }
  .person__title { font-size: 11px; color: var(--text-muted); margin-top: -2px; }

  .contacts { position: absolute; left: 40px; top: 168px; list-style: none; font-size: 11px; color: var(--text-blue); }
  .contacts li { display: flex; align-items: center; gap: 7px; line-height: 17px; white-space: nowrap; }
  .contacts svg { width: 11px; height: 11px; fill: var(--text-blue); flex: none; }
  .address { position: absolute; left: 40px; top: 230px; font-size: 11px; color: var(--text-blue); white-space: nowrap; }

  .socials { position: absolute; right: 22px; top: 168px; display: flex; gap: 5px; }
  .socials span { width: 17px; height: 17px; background: var(--social); display: block; }

  .band { position: absolute; left: 0; right: 0; bottom: 0; height: 14px; background: var(--band-light); }
  .band__deep { position: absolute; left: 0; bottom: 0; width: 58%; height: 14px; background: var(--brand-deep); clip-path: polygon(0 0, 100% 0, 96% 100%, 0 100%); }

  .back__brand { position: absolute; left: 70px; top: 155px; }
  .back__brand .brand__mark { background: #fff; }
  .back__brand .brand__name { font-size: 46px; color: #fff; }
  .back__tagline { position: absolute; left: 70px; top: 212px; color: #fff; }
  .back__url { position: absolute; right: 28px; top: 112px; font-size: 11px; color: #fff; white-space: nowrap; }
</style>
</head>
<body>
  <section class="card card--front" aria-label="Business card front">
    <div class="brand front__brand">
      <span class="brand__mark"></span>
      <span class="brand__name">velmit</span>
    </div>
    <p class="tagline front__tagline">Clear Water...Proven Care</p>
    <div class="person">
      <p class="person__name">Dana Whitlock</p>
      <p class="person__title">Director</p>
    </div>
    <ul class="contacts">
      <li><svg viewBox="0 0 24 24"><path d="M6.6 10.8a15 15 0 0 0 6.6 6.6l2.2-2.2a1 1 0 0 1 1-.25 11.4 11.4 0 0 0 3.6.57 1 1 0 0 1 1 1V20a1 1 0 0 1-1 1A17 17 0 0 1 3 4a1 1 0 0 1 1-1h3.5a1 1 0 0 1 1 1c0 1.25.2 2.45.57 3.57a1 1 0 0 1-.25 1z"/></svg>1-800-555-0142 (Toll Free)</li>
      <li><svg viewBox="0 0 24 24"><path d="M7 2h10a2 2 0 0 1 2 2v16a2 2 0 0 1-2 2H7a2 2 0 0 1-2-2V4a2 2 0 0 1 2-2zm0 3v13h10V5z"/></svg>555-210-0187</li>
      <li><svg viewBox="0 0 24 24"><path d="M2 5h20v14H2zm2 2v.5l8 5 8-5V7z"/></svg>dana@velmitpools.example</li>
    </ul>
    <p class="address">1280 Harbor Lane, Springfield, CA</p>
    <div class="socials" aria-label="Social links">
      <span></span><span></span><span></span><span></span>
    </div>
    <div class="band"><div class="band__deep"></div></div>
  </section>

  <section class="card card--back" aria-label="Business card back">
    <p class="back__url">www.velmitpools.example</p>
    <div class="brand back__brand">
      <span class="brand__mark"></span>
      <span class="brand__name">velmit</span>
    </div>
    <p class="tagline back__tagline">Clear Water...Proven Care</p>
  </section>
</body>
</html>
```